Insurance Law Website

**Please note do not sell insurance, we are a law firm which specialises in Insurance law.**

We are a legal insurance firm based in Australia consisting of 150+ legal professionals.

Our initial budget for this project is around: $500

We require a design to meet the specification below, however we do want designers to come up with an interpretation of something modern but still professional, we need it to stand out above all other legal websites!

1. Responsive design
2. It should be a minimalist design, the use of background imagery is fine but we are looking to de-clutter the home page in particular and have additional content accessible through menu links to other areas such as publications, news, announcements and expert/staff pages, careers etc.
3. Something that stands out from a typical legal website.
4. The homepage should cater for a video which will contain a 'who we are' message from the CEO/Firm.
5. Colours used light/medium blues (eg: #8aabff, #bdd7fc), white
6. We also require a static information box on the page with the heading "THREE STATES, ONE FOCUS" - see image attached for full text of the box.

Visitors to our website should be aware we are an Insurance law firm, this can be achieved by using insurance focused full background imagery (no natural disasters such as floods, earthquakes etc) such as insurance buildings (Harwick building - London), international landmarks etc

Some websites we like certain aspects of;

http://pellambraithwaite.com/ - top image boxes
http://www.vantel.com.au/ - similar however prefer to use a FULL background image, with one full width text box at the bottom, navigation menu at the top with logo

However please don't take these examples as a sign of what the site MUST look like, please use your imagination to interpret your own vision.

Reason: Extended due to feedback provided and waiting for resubmission of designs. It appears that some people may be misunderstanding the brief, please review the brief in full before submitting any designs and let us know if you have any questions.

Reason: Apologies to those who are waiting for a decision we are reviewing and discussiing all submitted designs internally and waiting for some additional amendments to come in. We have extended the project a final time whilst we carry out our reviews. Please continue to submit any modifications and thanks again for everyone's input thus far. D+T

We have 3 days left of this project please keep submitting your designs. This is a guaranteed project.

D+T

Target Market(s)

Lawyers looking for publications, information, contact details of our lawyers and careers/job searches.

Industry/Entity Type

Insurance

Font styles to use
Sans Serif

Requirements
Must have
• Top menu to include:

Home (small icon)
Who We Are (text)
Experts (text)
Expertise (text)
Media (text)
- News (text)
- Publications (text)
Community Footprint (text)
Careers (text)
Contact (text/icon)
Search (icon - will expand on click to search in field)

Footer to include:

Copyright (text)
Privacy Policy (text)
Cookie policy (text)
Sitemap (text)
Contact (text/icon)
Chainbook (icon)
Print (icon)
Email (icon)

Should not have
• Stereotypical imagery such as legal scales, money bags, natural disasters etc. We are a professional firm and require designs to suit.

```html
<!DOCTYPE html>
<html lang="en">
<head>
<meta charset="utf-8">
<title>hallam brook — Insurance Law</title>
<link href="https://fonts.googleapis.com/css2?family=Arimo:wght@400;700&display=swap" rel="stylesheet">
<style>
  :root{
    --brand-blue:#1e3f93;
    --nav-blue:#1d3d8c;
    --sky-light:#bdd7fc;
    --sky-mid:#8aabff;
    --band-dark:rgba(0,0,0,0.86);
    --band-soft:rgba(0,0,0,0.74);
    --white:#ffffff;
    --footer-bg:rgba(246,248,252,0.96);
  }
  *{margin:0;padding:0;box-sizing:border-box}
  html,body{width:1200px;height:900px;overflow:hidden}
  body{font-family:"Arimo",Arial,sans-serif;background:#eef2f8;position:relative}

  .site-header{position:absolute;left:0;top:0;width:1200px;height:132px;
    background:linear-gradient(180deg,#ffffff 0%,#eef2f8 100%)}
  .brand{position:absolute;left:36px;top:28px;color:var(--brand-blue);
    font-size:44px;line-height:38px;font-weight:400;letter-spacing:-0.5px}
  .main-nav{position:absolute;left:396px;top:92px;display:flex;align-items:center}
  .main-nav a{color:var(--nav-blue);text-decoration:none;font-size:15px;position:absolute;white-space:nowrap}

  .hero-photo{position:absolute;left:0;top:132px;width:1200px;height:701px;
    background:linear-gradient(160deg,#9fb3c8 0%,#5a6f86 30%,#2d3b4c 60%,#6f8599 85%,#aebfd0 100%)}

  .intro-band{position:absolute;left:0;top:172px;width:1200px;height:215px;background:var(--band-dark)}
  .intro-title{position:absolute;left:162px;top:30px;color:var(--white);font-size:42px;font-weight:400}
  .intro-title strong{font-weight:700}
  .intro-text{position:absolute;left:162px;top:98px;width:580px;color:var(--white);font-size:17px;line-height:24px}
  .video-panel{position:absolute;left:873px;top:26px;width:171px;height:171px;
    border:2px solid var(--sky-light);
    background:linear-gradient(180deg,#b9c2c9 0%,#6d7680 60%,#3a4048 100%)}
  .video-panel svg{position:absolute;left:0;top:0}

  .feature-band{position:absolute;left:0;top:398px;width:1200px;height:214px;background:var(--band-soft)}
  .feature{position:absolute;top:18px;width:260px;color:var(--white)}
  .feature h2{font-size:24px;font-weight:700;margin-bottom:10px}
  .feature p{font-size:16.5px;line-height:20px}
  .feature .read-more{display:block;margin-top:8px;color:var(--white);text-decoration:none;font-weight:700;font-size:16.5px}

  .site-footer{position:absolute;left:0;top:833px;width:1200px;height:67px;background:var(--footer-bg)}
  .copyright{position:absolute;left:52px;top:35px;font-size:12px;color:var(--nav-blue)}
  .footer-links a{position:absolute;top:34px;font-size:12px;color:var(--nav-blue);text-decoration:none}
  .footer-icons{position:absolute;left:1089px;top:31px;display:flex;gap:6px}
  .footer-icons span{display:block;width:21px;height:21px;background:var(--nav-blue)}
</style>
</head>
<body>
  <header class="site-header">
    <div class="brand">hallam<br>brook</div>
    <nav class="main-nav">
      <a href="#" style="left:0;top:-8px" aria-label="Home">
        <svg width="20" height="18" viewBox="0 0 20 18"><path d="M10 1 L19 9 H16 V17 H12 V12 H8 V17 H4 V9 H1 Z" fill="#5a6aa8"/></svg>
      </a>
      <a href="#" style="left:54px;top:-6px">Who We Are</a>
      <a href="#" style="left:168px;top:-6px">Experts</a>
      <a href="#" style="left:249px;top:-6px">Expertise</a>
      <a href="#" style="left:342px;top:-6px">Media</a>
      <a href="#" style="left:411px;top:-6px">Community</a>
      <a href="#" style="left:518px;top:-6px">Footprint</a>
      <a href="#" style="left:606px;top:-6px">Careers</a>
      <a href="#" style="left:690px;top:-6px">Contact</a>
      <a href="#" style="left:766px;top:-9px" aria-label="Search">
        <svg width="22" height="22" viewBox="0 0 22 22"><circle cx="9" cy="9" r="6.5" fill="none" stroke="#1d3d8c" stroke-width="2.5"/><line x1="14" y1="14" x2="20" y2="20" stroke="#1d3d8c" stroke-width="3" stroke-linecap="round"/></svg>
      </a>
    </nav>
  </header>

  <div class="hero-photo" role="img" aria-label="Full background photo of the Harwick building's steel and glass exterior"></div>

  <section class="intro-band">
    <h1 class="intro-title">Three states. <strong>One focus.</strong></h1>
    <p class="intro-text">Our sole focus is insurance law and we act for a diverse range of risk carriers, underwriting agents, brokers and corporate insureds relevant to litigious and general advisory services.</p>
    <div class="video-panel" role="img" aria-label="Video: 'who we are' message from the firm's CEO">
      <svg width="171" height="171" viewBox="0 0 171 171">
        <circle cx="85" cy="88" r="46" fill="rgba(255,255,255,0.15)" stroke="#ffffff" stroke-width="5"/>
        <path d="M72 64 L110 88 L72 112 Z" fill="#ffffff"/>
      </svg>
    </div>
  </section>

  <section class="feature-band">
    <article class="feature" style="left:160px">
      <h2>People</h2>
      <p>Lorem ipsum dolor sit amet, consectetur adipiscing elit. Vivamus quis luctus lectus, nec dictum ligula. Nunc feugiat pellentesque dolor viverra.</p>
      <a class="read-more" href="#">&gt; Read more</a>
    </article>
    <article class="feature" style="left:481px;top:24px">
      <h2>Careers</h2>
      <p>Lorem ipsum dolor sit amet, consectetur adipiscing elit. Vivamus quis luctus lectus, nec dictum ligula. Nunc feugiat pellentesque dolor viverra.</p>
      <a class="read-more" href="#">&gt; Read more</a>
    </article>
    <article class="feature" style="left:813px">
      <h2>News</h2>
      <p>Lorem ipsum dolor sit amet, consectetur adipiscing elit. Vivamus quis luctus lectus, nec dictum ligula. Nunc feugiat pellentesque dolor viverra.</p>
      <a class="read-more" href="#">&gt; Read more</a>
    </article>
  </section>

  <footer class="site-footer">
    <p class="copyright">© All rights reserved 2014</p>
    <div class="footer-links">
      <a href="#" style="left:800px">Privacy Policy</a>
      <a href="#" style="left:912px">Cookie policy</a>
      <a href="#" style="left:1023px">Sitemap</a>
    </div>
    <div class="footer-icons">
      <span aria-label="Contact">
        <svg width="21" height="21" viewBox="0 0 21 21"><circle cx="10.5" cy="7" r="3.2" fill="#fff"/><path d="M4 17 C4 12 17 12 17 17 Z" fill="#fff"/></svg>
      </span>
      <span aria-label="Chainbook"></span>
      <span aria-label="Print">
        <svg width="21" height="21" viewBox="0 0 21 21"><rect x="6" y="3" width="9" height="4" fill="#fff"/><rect x="3" y="8" width="15" height="7" fill="#fff"/><rect x="6" y="13" width="9" height="5" fill="#fff" stroke="#1d3d8c" stroke-width="1"/></svg>
      </span>
      <span aria-label="Email">
        <svg width="21" height="21" viewBox="0 0 21 21"><rect x="3" y="5" width="15" height="11" fill="#fff"/><path d="M3 5 L10.5 11 L18 5" fill="none" stroke="#1d3d8c" stroke-width="1.5"/></svg>
      </span>
    </div>
  </footer>
</body>
</html>
```